Hallowmere Business Card

This is the personal business card for Dr Glen Hallowmere and convers three area of his professional activity - all of them involve (foreign) languages:
o RQVB International Ltd - A translation company with 50 staff. Trades internationally
o TideLatch Ltd - a global online auction marketplace for translation services (startup)
o Vowelcraft - cutting edge technology from the brain sciences which helps learners assimilate the sound patterns of a new language (startup)

Target Market(s)

The card needs to have a "cutting edge" feel - but for a fairly conservative audience - academics, investors.

Industry/Entity Type

Business

Requirements
Must have
• Text:
Dr Glen Hallowmere

Co-founder RQVB International Ltd (Language translation)
Founder TideLatch Ltd (Translation marketplace)
Founder Vowelcraft (Language acquisition)

email: glen.morrow@lintmail.example
Phone: +64 21 555 3916
Twitter: @GlenMorrow4

```html
<!DOCTYPE html>
<html lang="en">
<head>
<meta charset="utf-8">
<title>Dr Glen Hallowmere – Business Card</title>
<link rel="stylesheet" href="https://fonts.googleapis.com/css2?family=Arimo:wght@400;700&family=EB+Garamond:wght@400;500&display=swap">
<style>
  :root {
    --olive: #a19e74;
    --maroon: #6a0000;
    --ink: #1c1c1c;
    --paper: #ffffff;
    --edge: #000000;
  }
  html, body {
    margin: 0;
    padding: 0;
    width: 1200px;
    height: 686px;
    overflow: hidden;
    background: var(--paper);
  }
  .card {
    position: relative;
    width: 1200px;
    height: 686px;
    font-family: "Arimo", Arial, sans-serif;
    color: var(--ink);
  }
  .card-edge {
    position: absolute;
    left: 35px;
    top: 34px;
    width: 1156px;
    height: 618px;
    border-right: 2px solid var(--edge);
    border-bottom: 2px solid var(--edge);
    box-sizing: border-box;
  }
  .band-top {
    position: absolute;
    left: 35px; top: 34px;
    width: 1070px; height: 96px;
    background: var(--olive);
    border: 1px solid #3a3a2a;
    box-sizing: border-box;
  }
  .corner-top {
    position: absolute;
    left: 1105px; top: 34px;
    width: 86px; height: 96px;
    background: var(--maroon);
    border: 1px solid #2a0000;
    box-sizing: border-box;
  }
  .band-name {
    position: absolute;
    left: 35px; top: 130px;
    width: 1070px; height: 64px;
    background: var(--maroon);
  }
  .corner-name {
    position: absolute;
    left: 1105px; top: 130px;
    width: 86px; height: 64px;
    background: var(--olive);
  }
  .side-bar {
    position: absolute;
    left: 35px; top: 194px;
    width: 16px; height: 458px;
    background: var(--maroon);
  }
  .band-title {
    position: absolute;
    left: 77px; top: 146px;
    margin: 0;
    font-family: "EB Garamond", "Times New Roman", serif;
    font-weight: 400;
    font-size: 27px;
    line-height: 32px;
    letter-spacing: 5px;
    color: var(--paper);
  }
  .roles {
    position: absolute;
    left: 77px; top: 262px;
    margin: 0; padding: 0;
    list-style: none;
    font-size: 16.5px;
    line-height: 25px;
    width: 480px;
  }
  .roles li { margin-bottom: 21px; }
  .contact {
    position: absolute;
    left: 77px; top: 442px;
    margin: 0;
    font-style: normal;
    font-size: 29px;
    line-height: 39px;
  }
  .contact span { display: block; }
  .person {
    position: absolute;
    left: 593px; top: 284px;
  }
  .person-name {
    margin: 0;
    font-weight: 700;
    font-size: 25px;
    line-height: 32px;
    color: var(--maroon);
  }
  .person-field {
    margin: 32px 0 0;
    font-size: 28px;
    line-height: 34px;
    color: #2a2a2a;
  }
</style>
</head>
<body>
  <main class="card">
    <div class="card-edge"></div>
    <div class="band-top"></div>
    <div class="corner-top"></div>
    <div class="band-name"></div>
    <div class="corner-name"></div>
    <div class="side-bar"></div>

    <h1 class="band-title">DR. GLEN HALLOWMERE</h1>

    <ul class="roles">
      <li>Co-founder RQVB International Ltd (Language<br>Translation)</li>
      <li>Founder TideLatch Ltd (Translation Marketplace)</li>
      <li>Founder Vowelcraft (Language Acquisition)</li>
    </ul>

    <address class="contact">
      <span>Phone: +64 21 555 3916</span>
      <span>Twitter: @GlenMorrow4</span>
      <span>E-mail: glen.morrow@lintmail.example</span>
    </address>

    <section class="person">
      <p class="person-name">Glen Hallowmere</p>
      <p class="person-field">Profession in Foreign Languages</p>
    </section>
  </main>
</body>
</html>
```